Project VOIP Phone

Vextara Antilles needs a advertisement design for a new product called a VOIP PHONE. A VOIP Phone stands for Voice Over Internet Protocol. The advantages in comparison with a PSTN (Packet-Switched Telephone Network) are that a VOIP system saves a lot of money. Besides that it is simple, flexible and is the future of telecom.
The text of the advertisement should be:
' Get your VOIP PHONE SYSTEM starting at ƒ 25,- per phone (p/m)'
'VOIP PHONE SYSTEM' and 'ƒ 25,-' should be bigger than the rest, '(p/m)' should be smaller than the rest.
Under that our contact data should follow:
Vextara Antilles
Tel: +599 9 732-1084
E-mail: sales@vextara.example
Website: www.vextara.example
The last rule of the Banner must contain a small text:
''Vextara Cloud Solotions & Management''
We want to receive an optional design with some watermarks in the back with 2 or 3 words like: "cheap'' ''solid'' or ''reliable'' ''up coming'' ''Future'' or something like that.
We also want some pictures (attached) in the banner. Not al the pictures are needed, just whatever looks best on it.
The banner must have a size of: 728x200.
Good luck!
Updates
Please help us with this interesting project in the future of telephony
Industry/Entity Type
Internet
Look and feel
Each slider illustrates characteristics of the customer's brand and the style your logo design should communicate.

```html
<!DOCTYPE html>
<html lang="en">
<head>
<meta charset="utf-8">
<title>Vextara Antilles – VOIP Phone System Banner</title>
<link rel="stylesheet" href="https://fonts.googleapis.com/css2?family=Mulish:wght@400;600&family=Arimo:ital,wght@0,400;0,700;1,400&display=swap">
<style>
  :root {
    --backdrop: #4c4948;
    --panel-light: #ffffff;
    --panel-shade: #e4e4e4;
    --side-panel: #f2f2f2;
    --brand-blue: #2aa3db;
    --deep-blue: #1f7fb8;
    --ink: #1c1c1c;
  }
  html, body {
    margin: 0;
    padding: 0;
    width: 1200px;
    height: 1200px;
    overflow: hidden;
    background: var(--backdrop);
  }
  .canvas {
    position: relative;
    width: 1200px;
    height: 1200px;
  }
  .banner {
    position: absolute;
    left: 66px;
    top: 454px;
    width: 1066px;
    height: 292px;
  }
  .tagline { font-family: "Mulish", sans-serif; font-weight: 400; fill: var(--brand-blue); }
  .voip-word { font-family: "Arimo", sans-serif; font-weight: 700; fill: url(#voipFill); stroke: var(--deep-blue); stroke-width: 1.5; }
  .headline { font-family: "Arimo", sans-serif; font-weight: 700; fill: var(--brand-blue); }
  .lead { font-family: "Arimo", sans-serif; font-weight: 400; fill: var(--brand-blue); }
  .price { font-family: "Arimo", sans-serif; font-weight: 400; fill: url(#priceFill); stroke: var(--deep-blue); stroke-width: 2; }
  .price-sign { font-style: italic; }
  .brand-name { font-family: "Mulish", sans-serif; font-weight: 600; fill: var(--brand-blue); }
  .contact { font-family: "Mulish", sans-serif; font-weight: 400; fill: var(--ink); }
</style>
</head>
<body>
<div class="canvas">
  <svg class="banner" viewBox="0 0 1066 292" width="1066" height="292" xmlns="http://www.w3.org/2000/svg">
    <defs>
      <radialGradient id="panelGlow" cx="0.33" cy="0.5" r="0.6">
        <stop offset="0" stop-color="var(--panel-light)"/>
        <stop offset="0.7" stop-color="#f1f1f1"/>
        <stop offset="1" stop-color="var(--panel-shade)"/>
      </radialGradient>
      <linearGradient id="priceFill" x1="0" y1="0" x2="0" y2="1">
        <stop offset="0" stop-color="#e9f7fe"/>
        <stop offset="1" stop-color="#7cc9ee"/>
      </linearGradient>
      <linearGradient id="voipFill" x1="0" y1="0" x2="0" y2="1">
        <stop offset="0" stop-color="#8fd3f3"/>
        <stop offset="1" stop-color="#2a8cc4"/>
      </linearGradient>
    </defs>

    <!-- main field -->
    <rect class="offer-panel" x="0" y="0" width="1066" height="292" fill="url(#panelGlow)"/>

    <!-- contact side with curved divider -->
    <path class="contact-panel" d="M721 0 Q790 146 721 292 L1066 292 L1066 0 Z" fill="var(--side-panel)"/>
    <path class="divider" d="M721 0 Q790 146 721 292" fill="none" stroke="#ffffff" stroke-width="6"/>

    <!-- offer -->
    <text class="tagline" x="259" y="46" font-size="25">Get your</text>
    <rect class="handset-art" x="140" y="138" width="82" height="60" rx="30" fill="#9fd6f1" opacity="0.5" role="img" aria-label="Telephone handset with coiled cord"/>
    <text class="voip-word" x="88" y="130" font-size="92" textLength="195" lengthAdjust="spacingAndGlyphs">VOIP</text>
    <text class="headline" x="288" y="114" font-size="43" textLength="395" lengthAdjust="spacingAndGlyphs">PHONE SYSTEM</text>
    <text class="lead" x="351" y="192" font-size="23" text-anchor="end">starting</text>
    <text class="lead" x="342" y="221" font-size="23" text-anchor="end">at</text>
    <text class="price" x="350" y="221" font-size="122"><tspan class="price-sign">ƒ</tspan>25</text>
    <text class="lead" x="400" y="254" font-size="18">per phone (p/m)</text>

    <!-- brand -->
    <rect class="brand-mark" x="912" y="26" width="94" height="84" rx="8" fill="var(--brand-blue)"/>
    <text class="brand-name" x="959" y="137" font-size="24" text-anchor="middle">vextara</text>

    <!-- contact details -->
    <g class="contact" font-size="19" text-anchor="end">
      <text x="1035" y="186">Vextara Antilles</text>
      <text x="1035" y="213">Tel: +599 9 732-1084</text>
      <text x="1035" y="239">E-mail: sales@vextara.example</text>
      <text x="1035" y="264">Website: www.vextara.example</text>
    </g>
  </svg>
</div>
</body>
</html>
```